Quick 1hr job to create exciting page header & footer designs

We need some exciting and engaging header and footer designs for school yearbooks, in particular for the NZ Primary school market (children 5 to 10 years old).
The header and footer designs need to be bright and colourful, and should appeal to younger children. Header and footer graphics do not need to be the same, but should at least relate to each other thematically.
Please include the following sample text on the header: Sports Day.
Please include this sample text on the footer: Primary School Name 2014.
Note that the header/footers may be used without the text so the design should work with or without the text. Header/footer may be used over top of a coloured or graphic background. The graphic could be illustrative, photographic or patterned, the more creative the better.

Header dimensions: 198.88 mm w x 15.24 mm h
Footer dimensions: 198.88 mm w x 6.35 mm h

Please see the example pages provided, but please note we are looking for something more suitable for Primary Schools, and a lot more dynamic and interesting!

Target Market(s)

New Zealand Primary Schools

Industry/Entity Type

School

Requirements
Must have
• Must contain sample text and must be suitable for younger children
• Must be appropriate for the New Zealand market, i.e. don't use imagery that is obviously from other countries.

```html
<!DOCTYPE html>
<html lang="en">
<head>
<meta charset="utf-8">
<title>Sports Day – Yearbook Header</title>
<link rel="stylesheet" href="https://fonts.googleapis.com/css2?family=Alfa+Slab+One&display=swap">
<style>
  :root {
    --sky: #c9eef8;
    --sky-line: #bde6f3;
    --ink: #111111;
    --shadow: #3a3a3a;
    --pink: #f18ad2;
    --yellow: #f6ec86;
    --green: #b9ef93;
    --cyan: #95e3f2;
    --violet: #a58ef0;
  }
  html, body {
    margin: 0;
    padding: 0;
    width: 1200px;
    height: 92px;
    overflow: hidden;
    background: var(--sky);
  }
  .header-banner {
    position: relative;
    width: 1200px;
    height: 92px;
    overflow: hidden;
    background:
      repeating-linear-gradient(to bottom,
        var(--sky) 0px, var(--sky) 3px,
        var(--sky-line) 3px, var(--sky-line) 4px);
  }
  .header-art {
    position: absolute;
    inset: 0;
    display: block;
  }
  .title-text {
    font-family: "Alfa Slab One", Georgia, serif;
    font-size: 58px;
  }
</style>
</head>
<body>
  <header class="header-banner">
    <svg class="header-art" width="1200" height="92" viewBox="0 0 1200 92" xmlns="http://www.w3.org/2000/svg">
      <defs>
        <linearGradient id="rainbow-bands" gradientUnits="userSpaceOnUse" x1="520" y1="0" x2="1140" y2="0">
          <stop offset="0" stop-color="#c9eef8" stop-opacity="0"/>
          <stop offset="0.05" stop-color="#f18ad2"/>
          <stop offset="0.10" stop-color="#f6ec86"/>
          <stop offset="0.15" stop-color="#b9ef93"/>
          <stop offset="0.20" stop-color="#95e3f2"/>
          <stop offset="0.25" stop-color="#f18ad2"/>
          <stop offset="0.52" stop-color="#f18ad2"/>
          <stop offset="0.57" stop-color="#f6ec86"/>
          <stop offset="0.62" stop-color="#b9ef93"/>
          <stop offset="0.67" stop-color="#95e3f2"/>
          <stop offset="0.72" stop-color="#f18ad2"/>
          <stop offset="0.86" stop-color="#f3a6dc"/>
          <stop offset="0.93" stop-color="#a8ebe4"/>
          <stop offset="1" stop-color="#c9eef8" stop-opacity="0"/>
        </linearGradient>
        <linearGradient id="title-fill" gradientUnits="userSpaceOnUse" x1="50" y1="0" x2="530" y2="0">
          <stop offset="0" stop-color="#b9ef93"/>
          <stop offset="0.2" stop-color="#e9f27f"/>
          <stop offset="0.38" stop-color="#f38ab8"/>
          <stop offset="0.55" stop-color="#f5a0b4"/>
          <stop offset="0.75" stop-color="#c59be8"/>
          <stop offset="1" stop-color="#a58ef0"/>
        </linearGradient>
      </defs>

      <g class="diagonal-bands" transform="skewX(45)">
        <rect x="520" y="0" width="620" height="92" fill="url(#rainbow-bands)"/>
      </g>

      <g class="title">
        <text class="title-text" x="56" y="67" textLength="482" lengthAdjust="spacingAndGlyphs"
              fill="var(--shadow)" stroke="var(--shadow)" stroke-width="3" opacity="0.85">Sports Day</text>
        <text class="title-text" x="50" y="62" textLength="482" lengthAdjust="spacingAndGlyphs"
              fill="url(#title-fill)" stroke="var(--ink)" stroke-width="2.5" paint-order="stroke">Sports Day</text>
      </g>
    </svg>
  </header>
</body>
</html>
```